Debt Relief Landing Page Design

I need a landing page designed (and the accompanying Thank You page) for my client.

I have drafted the wireframes for the layout of the pages (attached) and need a professional looking finish.

The main colours to use are green and blue as per their current branding, see website for specifications - http://www.clearpathledger.com.au/

```html
<!DOCTYPE html>
<html lang="en">
<head>
<meta charset="utf-8">
<title>ClearPath Ledger – Debt Consolidation</title>
<link href="https://fonts.googleapis.com/css2?family=Open+Sans:ital,wght@0,400;0,600;0,700;0,800;1,400&display=swap" rel="stylesheet">
<style>
:root{
  --green:#5aa832;
  --green-dark:#468a24;
  --blue:#1d63a8;
  --teal:#3db2c0;
  --navy:#1d3a58;
  --client-blue:#2e8fd0;
  --client-blue-dark:#2379b6;
  --footer:#2b3038;
  --ink:#333;
  --muted:#666;
  --white:#fff;
}
*{box-sizing:border-box;margin:0;padding:0}
html,body{width:1200px;height:2196px;overflow:hidden}
body{font-family:"Open Sans",Arial,sans-serif;color:var(--ink);background:var(--white);position:relative}

.site-header{height:100px;display:flex;justify-content:space-between;align-items:center;padding:0 40px}
.brand{display:flex;align-items:center;gap:12px;font-size:34px;font-weight:800;color:var(--green)}
.brand-mark{width:18px;height:18px;background:var(--blue)}
.contact{text-align:right;font-size:30px;line-height:1.1;color:var(--ink)}

.hero{background:var(--teal);height:520px;position:relative;color:var(--white);padding:40px 40px}
.hero-copy{width:700px}
.hero h1{font-size:38px;font-weight:800;margin-bottom:20px}
.hero h2{font-size:26px;font-weight:700;text-align:center;line-height:1.35;margin-bottom:28px}
.hero p{font-size:15px;line-height:1.55;margin-bottom:14px}

.consult-form{position:absolute;right:60px;top:20px;width:350px;background:var(--navy);padding:22px 22px 26px}
.consult-form h3{text-align:center;font-size:24px;font-weight:600;margin-bottom:6px}
.consult-form .note{text-align:center;font-size:12px;line-height:1.35;margin-bottom:18px;color:#d6e2ee}
.field{display:flex;align-items:center;margin-bottom:10px}
.field label{width:110px;font-size:14px}
.field span{flex:1;background:var(--white);color:#999;font-size:13px;padding:8px 10px}
.btn{display:block;background:var(--green);color:var(--white);font-weight:600;text-align:center;border-radius:4px;border-bottom:3px solid var(--green-dark)}
.consult-form .btn{margin:18px auto 0;width:220px;font-size:17px;padding:14px 0}

.services{height:740px;padding-top:90px;text-align:center}
.section-title{font-size:26px;font-weight:700;color:var(--green)}
.rule{width:1040px;height:1px;background:#ccc;margin:20px auto 40px}
.service-grid{display:grid;grid-template-columns:repeat(3,300px);column-gap:60px;row-gap:50px;justify-content:center}
.service-icon{width:56px;height:56px;border-radius:50%;background:#efe3c8;margin:0 auto 16px}
.service h4{font-size:18px;font-weight:700;margin-bottom:8px}
.service p{font-size:13px;line-height:1.45;color:var(--muted)}
.services .btn{width:300px;margin:60px auto 0;font-size:20px;padding:18px 0}

.clients{background:var(--client-blue);height:780px;color:var(--white);text-align:center}
.clients-head{background:var(--client-blue-dark);height:70px;line-height:70px;font-size:28px;font-weight:700}
.testimonials{display:grid;grid-template-columns:repeat(3,300px);column-gap:90px;row-gap:36px;justify-content:center;padding-top:20px}
.avatar{width:110px;height:110px;border-radius:50%;background:#1c4f7a;border:3px solid #9cc8ea;margin:0 auto 14px}
.quote{font-size:13px;line-height:1.5;text-align:left;font-style:italic;padding:0 30px}
.author{font-size:11px;text-align:right;padding:6px 30px 0;color:#d9ecfa}
.clients .btn{width:300px;margin:34px auto 0;font-size:20px;padding:16px 0}

.site-footer{position:absolute;left:0;bottom:0;width:1200px;height:56px;background:var(--footer);color:#bbb;font-size:13px;display:flex;justify-content:space-between;align-items:center;padding:0 40px}
.site-footer a{color:#8fc3ea;text-decoration:none}
</style>
</head>
<body>

<header class="site-header">
  <div class="brand"><span class="brand-mark"></span>ClearPath Ledger</div>
  <div class="contact">Contact us on:<br>1300 555 214</div>
</header>

<section class="hero">
  <div class="hero-copy">
    <h1>Looking To Consolidate Your Debt?</h1>
    <h2>If You Have Over $10,000 In Debt, We Can<br>Help You To Be Debt Free In 3-5 Years.</h2>
    <p>ClearPath Ledger is Australia's debt help relief specialists. Through years of industry experience and knowledge, our team of debt management experts can actively advise you on how to get out of the red, fast.</p>
    <p>At ClearPath Ledger we are able to actively rectify your debt problems by creating simple and affordable payment plans for all debts.</p>
    <p>To get a free, no obligation consultation by one of our industry leading experts, as well as a Debt Management Plan, simply fill out the form on the right and we will be in contact with you within 48 hours.</p>
  </div>

  <form class="consult-form">
    <h3>Free Consultation</h3>
    <p class="note">Fill In The Form Below To Receive Your Free, No Obligation Consultation</p>
    <div class="field"><label>Name</label><span>Enter Name</span></div>
    <div class="field"><label>Phone</label><span>Enter Phone No.</span></div>
    <div class="field"><label>Email</label><span>Enter Your Email</span></div>
    <div class="field"><label>Post Code</label><span>Enter Post Code</span></div>
    <div class="field"><label>Unsecured Debt</label><span>Enter Unsecured Debt</span></div>
    <div class="field"><label>Preferred Call Time</label><span>Enter Preferred Call Time</span></div>
    <span class="btn">Get My Free Consultation</span>
  </form>
</section>

<section class="services">
  <h2 class="section-title">Some Of Our Debt Relief Services</h2>
  <div class="rule"></div>
  <div class="service-grid">
    <div class="service"><div class="service-icon" role="img" aria-label="Service icon"></div><h4>Debt Consolidation Loan</h4><p>Stop getting hassled by creditors. Let us consolidate your personal debts into one easy repayment plan.</p></div>
    <div class="service"><div class="service-icon" role="img" aria-label="Service icon"></div><h4>Debt Consolidation Loan</h4><p>Stop getting hassled by creditors. Let us consolidate your personal debts into one easy repayment plan.</p></div>
    <div class="service"><div class="service-icon" role="img" aria-label="Service icon"></div><h4>Debt Consolidation Loan</h4><p>Stop getting hassled by creditors. Let us consolidate your personal debts into one easy repayment plan.</p></div>
    <div class="service"><div class="service-icon" role="img" aria-label="Service icon"></div><h4>Debt Consolidation Loan</h4><p>Stop getting hassled by creditors. Let us consolidate your personal debts into one easy repayment plan.</p></div>
    <div class="service"><div class="service-icon" role="img" aria-label="Service icon"></div><h4>Debt Consolidation Loan</h4><p>Stop getting hassled by creditors. Let us consolidate your personal debts into one easy repayment plan.</p></div>
    <div class="service"><div class="service-icon" role="img" aria-label="Service icon"></div><h4>Debt Consolidation Loan</h4><p>Stop getting hassled by creditors. Let us consolidate your personal debts into one easy repayment plan.</p></div>
  </div>
  <span class="btn">Get My Free Consultation</span>
</section>

<section class="clients">
  <h2 class="clients-head">What Clients Say</h2>
  <div class="testimonials">
    <div class="testimonial"><div class="avatar" role="img" aria-label="Client portrait placeholder"></div><p class="quote">We were on the verge of losing our car and did not know what to do. The team set up an affordable arrangement to catch up on our payments and put us on the way to debt freedom. We are now thinking of buying a house.</p><p class="author">- A Verified Client, NSW</p></div>
    <div class="testimonial"><div class="avatar" role="img" aria-label="Client portrait placeholder"></div><p class="quote">We were on the verge of losing our car and did not know what to do. The team set up an affordable arrangement to catch up on our payments and put us on the way to debt freedom. We are now thinking of buying a house.</p><p class="author">- A Verified Client, VIC</p></div>
    <div class="testimonial"><div class="avatar" role="img" aria-label="Client portrait placeholder"></div><p class="quote">We were on the verge of losing our car and did not know what to do. The team set up an affordable arrangement to catch up on our payments and put us on the way to debt freedom. We are now thinking of buying a house.</p><p class="author">- A Verified Client, QLD</p></div>
    <div class="testimonial"><div class="avatar" role="img" aria-label="Client portrait placeholder"></div><p class="quote">We were on the verge of losing our car and did not know what to do. The team set up an affordable arrangement to catch up on our payments and put us on the way to debt freedom. We are now thinking of buying a house.</p><p class="author">- A Verified Client, WA</p></div>
    <div class="testimonial"><div class="avatar" role="img" aria-label="Client portrait placeholder"></div><p class="quote">We were on the verge of losing our car and did not know what to do. The team set up an affordable arrangement to catch up on our payments and put us on the way to debt freedom. We are now thinking of buying a house.</p><p class="author">- A Verified Client, SA</p></div>
    <div class="testimonial"><div class="avatar" role="img" aria-label="Client portrait placeholder"></div><p class="quote">We were on the verge of losing our car and did not know what to do. The team set up an affordable arrangement to catch up on our payments and put us on the way to debt freedom. We are now thinking of buying a house.</p><p class="author">- A Verified Client, TAS</p></div>
  </div>
  <span class="btn">Get My Free Consultation</span>
</section>

<footer class="site-footer">
  <span>© 2008 &amp; 2015 - All rights reserved. <a href="http://www.clearpathledger.com.au/">Terms and Conditions</a></span>
  <a href="http://www.clearpathledger.com.au/">Privacy Policy</a>
</footer>

</body>
</html>
```